Website for online Real Estate School

I need to have three drop boxes which are really the main item on our web site. These tabs will need to be front and center “call to action”. Our sole goal on our site is to sell real estate courses which will be connected to these drop boxes. So please make this “call to action” section “clean” and the main emphasis on the page. We will fill in the items in the drop box so please ensure we have that ability.

 Get your license
 Post-Licensing
 Continuing Education

You could use the statement; “The Path to Your Future”

I’d like the design to be one where you keep scrolling down instead of having 5 or 6 tabs up top with different pages.

As you scan down I’d like to include the graphics and text as shown on one of the attachments. I copied this from another site so I’d ask you provide another logo. I already amended the text

People enter the real estate field with diverse educational backgrounds and overall goals. Some enter to only work part time to supplement their current income, and others full time. One person may enter the commercial market space and another residential. There is a wide range of directions you can take and the sky is truly the limit. Whichever path you take, your chances of success are directly related to your level of preparation and commitment. This is one career that really rewards self-motivated individuals.

 Careers - Career fields include residential and commercial real estate agents, brokers, mortgage brokers, property managers and independent investors. Many of these careers are held by independent people who have a strong entrepreneurial spirit. As you enter the real estate business in general its not unlikely you will be in it for life in one way or another. In our opinion it truly is the best path to wealth.
 Salary - According to the U.S. Office of Workforce Tallies, real estate brokers earned a median annual wage of $56,860 and the highest 10 percent earned more than $166,940. An agent’s income is only limited to how much work you want to put into your business. We highly suggest you consider a few of our partners offers below as they can truly help you work smarter, not harder.
 Degrees - A real estate license will provide all you will need to enter the real estate business. Each state has requirements that you complete “Continuing Education” every other year. There are several other courses that will provide you with certifications which demonstrate your sophistication therefore we recommend you continue your pursuit of education and we certainly hope you do so with us.

We highly recommend you consider a few of out strategic partners as their services are a tremendous advantage to real estate professionals.

Here we will have 6-8 banners from companies that we will be affiliates with.

At this point I’m not interested in providing an address nor phone number for contact.

Our web site domain is; www.HarborlineLearning.com

I have a number of graphics that I will upload the .ai file. Feel free to improve as you see fit.

I included a few copies of our competition. PLEASE, do some basic research.... in short, we are a national school that sells real estate licensing education for your initial license and also continuing education. We sooooooo want to be better than our competitors. Please help us achieve this. google real estate license and real estate continuing education and look at competitors... Please. That way you truly know what we need to beat.

This is my 40th ish project on pixel forum and appreciate everyone's work which is why I always come back.

We will be EXTREMELY RESPONSIVE AND LOG ON 5-10X A DAY TO COMMENT ON DESIGNS. PLEASE ONLY MESSAGE US ON THE DESIGN ITSELF VS VIA THE MAIL SYSTEM AS ITS EASIER FOR US. THANKS!!!

Reason: We have extended this project for 5 days as we think 2 days was a bit ambitious. We look forward to your designs

Target Market(s)

18-40 year old consumers. Aspiring and existing real estate agents and brokers

Industry/Entity Type

Real Estate

Coding

Coded - Design and coding required

Number of Pages Required

1 page

Font styles to use
Other font styles liked:
• your choice

Requirements
Must have
• clean site... please review the competition by searching on google; real estate continuing education and real estate license
Nice to have
• just clean site. nice and simple and be sure to have the call to action sections as the emphasis

```html
<!DOCTYPE html>
<html lang="en">
<head>
<meta charset="utf-8">
<title>Harborline Learning</title>
<link rel="stylesheet" href="https://fonts.googleapis.com/css2?family=Open+Sans:wght@400;600;700&family=Roboto+Slab:wght@700&display=swap">
<style>
:root{
  --orange:#ef6a12;
  --orange-dark:#d9550a;
  --ink:#2d2d2d;
  --muted:#6b6b6b;
  --band:#f3f3f3;
  --footer:#333333;
  --footer-deep:#2a2a2a;
  --line:#4a4a4a;
  --white:#ffffff;
}
*{box-sizing:border-box;margin:0;padding:0}
html,body{width:691px;height:1200px;overflow:hidden;background:var(--white)}
body{position:relative;font-family:"Open Sans",Arial,sans-serif;color:var(--ink)}
.abs{position:absolute}

/* header */
.site-header{left:0;top:0;width:691px;height:50px;background:var(--white);border-bottom:1px solid #ddd}
.brand{left:57px;top:30px;display:flex;align-items:center;gap:6px}
.brand-dot{width:12px;height:12px;border-radius:50%;background:var(--orange)}
.brand-name{font-weight:700;font-size:10.5px;letter-spacing:.3px;color:#4a3a2a;line-height:12px}
.nav a{position:absolute;top:20px;font-size:9px;color:var(--orange);text-decoration:none;white-space:nowrap}

/* hero */
.hero{left:0;top:50px;width:691px;height:329px;background:linear-gradient(100deg,#9a9fa3 0%,#c9cccf 45%,#d9dadb 70%,#a7abae 100%)}
.hero-title{left:57px;top:176px;font-family:"Roboto Slab",Georgia,serif;font-size:25px;font-weight:700;color:var(--white);letter-spacing:.5px;text-shadow:0 1px 3px rgba(0,0,0,.35);white-space:nowrap}
.hero-text{left:59px;top:212px;width:240px;font-size:8px;line-height:12px;color:var(--white)}
.hero-arrow{width:20px;height:20px;border-radius:50%;background:rgba(50,50,50,.7)}

/* call to action */
.cta{left:57px;top:313px;width:577px;height:66px;background:repeating-linear-gradient(45deg,#e2ddd5 0 2px,#f1eee9 2px 5px)}
.cta-inner{left:6px;top:6px;width:565px;height:56px;background:#faf8f5}
.cta-select{top:16px;width:138px;height:25px;background:var(--white);border:1px solid #e1ddd7;border-radius:2px;font-size:6.5px;color:#555;padding:8px 9px;white-space:nowrap}
.cta-select svg{position:absolute;right:9px;top:10px}
.cta-button{left:466px;top:16px;width:89px;height:25px;background:linear-gradient(90deg,var(--orange),#f47a26);color:var(--white);font-size:7px;text-align:center;line-height:25px;letter-spacing:.3px}

/* welcome */
.section-title{width:691px;text-align:center;font-size:18.5px;font-weight:400;color:var(--ink)}
.section-title span{color:var(--orange)}
.title-rule{left:197px;top:434px;width:297px;height:2px;border-top:1px dashed #ccc}
.lead{left:88px;width:516px;text-align:center;font-size:6.3px;line-height:12px;color:#444}
.feature{width:170px;text-align:center}
.feature-icon{margin:0 auto;width:64px;height:64px;border-radius:50%;background:radial-gradient(circle at 35% 30%,#f7a23a,#e8780f 60%,#d05f06);display:flex;align-items:center;justify-content:center}
.feature-title{margin-top:13px;font-size:10.5px;font-weight:600;color:#222}
.feature-text{margin-top:6px;font-size:6.3px;line-height:12px;color:#666}

/* services */
.services{left:0;top:668px;width:691px;height:270px;background:var(--band);border-top:1px solid #e8e8e8}
.service-rule{left:130px;top:756px;width:431px;height:1px;background:#e2e2e2}
.service-card{top:776px;height:128px}
.service-label{position:absolute;left:6px;top:92px;width:94px;height:18px;background:rgba(255,255,255,.88);font-size:8.5px;line-height:18px;padding-left:6px;color:#333}

/* contact strip */
.footer{left:0;top:999px;width:691px;height:163px;background:var(--footer)}
.contact{left:57px;top:962px;width:577px;height:67px;background:repeating-linear-gradient(45deg,#e2ddd5 0 2px,#f1eee9 2px 5px)}
.contact-inner{left:5px;top:5px;width:567px;height:57px;background:var(--white)}
.contact-item{left:0;top:18px;width:567px;display:flex;justify-content:center;align-items:center;gap:9px}
.contact-icon{width:19px;height:19px;border-radius:50%;border:1px solid #555;display:flex;align-items:center;justify-content:center}
.contact-text{font-size:8px;line-height:11px;color:#333}

/* footer columns */
.col-divider{top:1029px;width:1px;height:133px;background:var(--line)}
.footer-heading{top:1049px;font-size:8.5px;font-weight:400;color:var(--white);letter-spacing:.2px}
.footer-list{top:1069px;list-style:none;font-size:6.8px;line-height:12.8px;color:#ddd}
.footer-list li::before{content:"\203A";margin-right:7px;color:#ccc}
.footer-note{left:506px;top:1068px;width:130px;font-size:6.5px;line-height:11px;color:#ddd}
.news-input{left:506px;width:130px;height:24px;border:1px solid #4b4b4b;font-size:5.8px;color:#777;padding:8px 8px}
.subscribe{left:584px;top:1126px;width:52px;height:23px;background:var(--orange-dark);color:var(--white);font-size:6px;text-align:center;line-height:23px}
.copyright{left:0;top:1162px;width:691px;height:38px;background:var(--footer-deep);border-top:1px solid #444;color:#eee;font-size:7px;text-align:center;line-height:38px;font-family:Arial,sans-serif}
</style>
</head>
<body>

<header class="site-header abs">
  <div class="brand abs"><span class="brand-dot"></span><span class="brand-name">HARBORLINE LEARNING</span></div>
  <nav class="nav">
    <a style="left:300px">Home</a>
    <a style="left:356px">About us</a>
    <a style="left:420px">Salary</a>
    <a style="left:472px">Careers</a>
    <a style="left:529px">Degeree</a>
    <a style="left:592px">Contact Us</a>
  </nav>
</header>

<section class="hero abs" role="img" aria-label="Photo of two young professionals reviewing a laptop together in a bright office"></section>
<h1 class="hero-title abs">TO PATH TO YOUR FUTURE</h1>
<p class="hero-text abs">Lorem ipsum dolor sit amet, consectetur adipiscing elit, sed do eiusmod tempor incididunt ut labore adipiscing elit, sed do eiusmod tempor incididunt ut labore</p>
<div class="hero-arrow abs" style="left:21px;top:216px"><svg width="20" height="20"><path d="M11.5 6 L7.5 10 L11.5 14" fill="none" stroke="#fff" stroke-width="1.6"/></svg></div>
<div class="hero-arrow abs" style="left:653px;top:216px"><svg width="20" height="20"><path d="M8.5 6 L12.5 10 L8.5 14" fill="none" stroke="#fff" stroke-width="1.6"/></svg></div>

<div class="cta abs">
  <div class="cta-inner abs">
    <div class="cta-select abs" style="left:15px">Get your license<svg width="6" height="4"><path d="M0 0 L3 3 L6 0" fill="none" stroke="#888"/></svg></div>
    <div class="cta-select abs" style="left:165px">Post-Licensing<svg width="6" height="4"><path d="M0 0 L3 3 L6 0" fill="none" stroke="#888"/></svg></div>
    <div class="cta-select abs" style="left:315px">Continuing Education<svg width="6" height="4"><path d="M0 0 L3 3 L6 0" fill="none" stroke="#888"/></svg></div>
    <div class="cta-button abs">GET STARTED</div>
  </div>
</div>

<h2 class="section-title abs" style="left:0;top:401px">WELCOME TO <span>HARBORLINE LEARNING</span></h2>
<div class="title-rule abs"></div>
<p class="lead abs" style="top:447px">Lorem ipsum dolor sit amet, consectetur adipiscing elit, sed do eiusmod tempor incididunt ut labore et dolore magna aliqua. Ut enim ad minim veniam, quis nostrud exercitation ullamco laboris nisi ut aliquip ex ea commodo consequat. Duis aute irure dolor in reprehenderit in voluptate velit esse cillum dolore eu fugiat nulla pariatur. Excepteur sint occaecat cupidatat non proident, sunt in culpa qui officia deserunt mollit anim id est laborum</p>

<div class="feature abs" style="left:58px;top:508px">
  <div class="feature-icon"><svg width="26" height="26" viewBox="0 0 26 26"><path d="M8 4 H18 V9 H15 V22 L9 17 V9 H8 Z" fill="none" stroke="#fff" stroke-width="2" stroke-linejoin="round"/></svg></div>
  <div class="feature-title">Get your license</div>
  <p class="feature-text">Lorem ipsum dolor sit amet, consectetur adipising elit, sed do eiusmod tempor iunt ut labore et dolore magna aliqua. eiusmod</p>
</div>
<div class="feature abs" style="left:261px;top:508px">
  <div class="feature-icon"><svg width="26" height="26" viewBox="0 0 26 26"><rect x="3" y="8" width="20" height="13" rx="2" fill="#fff"/><path d="M10 8 V5 H16 V8" fill="none" stroke="#fff" stroke-width="2"/><path d="M8 8 V21 M18 8 V21" stroke="#e8780f" stroke-width="1.2"/></svg></div>
  <div class="feature-title">Post-Licensing</div>
  <p class="feature-text">Lorem ipsum dolor sit amet, consectetur adipising elit, sed do eiusmod tempor iunt ut labore et dolore magna aliqua. eiusmod</p>
</div>
<div class="feature abs" style="left:464px;top:508px">
  <div class="feature-icon"><svg width="26" height="26" viewBox="0 0 26 26"><path d="M7 4 H20 L18 20 H5 Z" fill="none" stroke="#fff" stroke-width="2" stroke-linejoin="round"/><path d="M9 9 H16 M8.5 13 H15.5" stroke="#fff" stroke-width="1.6"/><path d="M5 20 Q4 23 7 23 H18" fill="none" stroke="#fff" stroke-width="2"/></svg></div>
  <div class="feature-title">Continuing Education</div>
  <p class="feature-text">Lorem ipsum dolor sit amet, consectetur adipising elit, sed do eiusmod tempor iunt ut labore et dolore magna aliqua. eiusmod</p>
</div>

<section class="services abs"></section>
<h2 class="section-title abs" style="left:0;top:693px">OUR <span>SERVICES</span></h2>
<p class="lead abs" style="left:128px;width:435px;top:723px">Lorem ipsum dolor sit amet, consectetur adipiscing elit, sed do eiusmod tempor incididunt ut labore et dolore magna aliqua. Ut enim ad minim veniam, quis nostrud exercitation ullamco laboris nisi ut aliquip ex ea commodo consequat. Duis aute irure</p>
<div class="service-rule abs"></div>

<div class="service-card abs" style="left:57px;width:162px;background:linear-gradient(135deg,#4e5c6a,#8a8f95 55%,#5a4a40)" role="img" aria-label="Photo of professionals at a table with career and training words drawn around them"><div class="service-label">Careers</div></div>
<div class="service-card abs" style="left:257px;width:169px;background:linear-gradient(135deg,#d8d8d8,#c6b89f 55%,#e3e3e3)" role="img" aria-label="Photo of a businessman beside a large money sack"><div class="service-label" style="left:11px">Salary</div></div>
<div class="service-card abs" style="left:471px;width:161px;background:linear-gradient(135deg,#2a2a2e,#b9a8a8 50%,#a8262b)" role="img" aria-label="Photo of graduates holding rolled diplomas tied with red ribbon"><div class="service-label">Degeree</div></div>

<footer class="footer abs"></footer>
<div class="contact abs">
  <div class="contact-inner abs">
    <div class="contact-item abs">
      <div class="contact-icon"><svg width="10" height="8" viewBox="0 0 10 8"><rect x=".5" y=".5" width="9" height="7" fill="none" stroke="#444"/><path d="M.5 .5 L5 4.5 L9.5 .5" fill="none" stroke="#444"/></svg></div>
      <div class="contact-text">Email :<br>hello@harborline.com</div>
    </div>
  </div>
</div>

<div class="col-divider abs" style="left:172px"></div>
<div class="col-divider abs" style="left:332px"></div>
<div class="col-divider abs" style="left:484px"></div>

<h3 class="footer-heading abs" style="left:58px">ABOUT US</h3>
<ul class="footer-list abs" style="left:58px;width:108px"><li style="padding-left:12px;text-indent:-12px">Lorem ipsum is deummy text on the all side of humer that is the crct pathu of vijay doo or die.</li></ul>

<h3 class="footer-heading abs" style="left:212px">DUMMY HEADING</h3>
<ul class="footer-list abs" style="left:212px"><li>Home</li><li>About Us</li><li>Careers</li><li>Degeree</li><li>Salary</li><li>Contact</li></ul>

<h3 class="footer-heading abs" style="left:370px;color:#ccc">LINKS</h3>
<ul class="footer-list abs" style="left:370px"><li>Link 1</li><li>Link 2</li><li>Link 3</li><li>Link 4</li><li>Link 5</li><li>Link 6</li></ul>

<h3 class="footer-heading abs" style="left:506px">SIGN UP FOR NEWSLETTER</h3>
<p class="footer-note abs">Excepteur sint occaecat cupidatat non dent, sunt in culpa qui officia</p>
<div class="news-input abs" style="top:1096px">Enter Name</div>
<div class="news-input abs" style="top:1126px;height:23px">Enter Email</div>
<div class="subscribe abs">SUBSCRIBE</div>

<div class="copyright abs">© 2016 real estate. All Rights Reserved.</div>

</body>
</html>
```